ROB & JO’S GOODBYE TO MIDGE BITES

I require an attractive appealing label with the dimensions 7.5m x 3.5cm
This is a Natural sandfly insect repellent cream formulated by 2 pharmacists Carla Whitby and Rob Kettering. It is required for labelling a 50 g jar

Contains Essential Oils of cedar wood, rosemary, cinnamon, citronella, lavender, eucalyptus and clove in a moisturising base.

We would like to see designs using the colour bright duck egg blue as the main colour with dark brown tones for the patterns. An eye catching label is output aim . However any colour combination that is attractive to the eye is welcome
A gloss finish is preferable.

More designs please

Target Market(s)

Trekkers, outdoor active people, pharmacy, health shops

Colors
abd037
34a6d7
0456a4
33b8a4

Requirements
Must have
• Rob and Jo’s
• Goodbye to Midge bites
• Natural Sandfly Repellent
• Contains Essential Oils of cedar wood, rosemary, cinnamon, citronella, lavender, eucalyptus and clove in a moisturising base.
• Formulated by Australian Pharmacists Carla Whitby and Rob Kettering
• Made in Australia
• 0413862207
Nice to have
• Sandfly/ flies
• I have attached a label I use for my mozzie cream and would like a similar font please

```html
<!DOCTYPE html>
<html lang="en">
<head>
<meta charset="utf-8">
<title>Rob and Jo’s Goodbye to Midge Bites – Natural Sandfly Repellent Label</title>
<link rel="stylesheet" href="https://fonts.googleapis.com/css2?family=Dancing+Script:wght@700&family=Fira+Sans+Extra+Condensed:wght@400;500;800&family=Open+Sans:wght@600&display=swap">
<style>
  :root {
    --teal: #2bb7a6;
    --teal-bright: #33b8a4;
    --ocean: #1f8fb4;
    --deep-blue: #1667ad;
    --brown: #744a2a;
    --brown-shadow: #4e3018;
    --white: #ffffff;
    --cream: #ecd98c;
    --shade: rgba(10, 50, 80, 0.45);
    --path: rgba(20, 50, 70, 0.55);
  }
  * { margin: 0; padding: 0; box-sizing: border-box; }
  html, body { width: 1200px; height: 558px; overflow: hidden; background: #fff; }

  .label {
    position: relative;
    width: 1200px;
    height: 558px;
    overflow: hidden;
    background: linear-gradient(125deg, var(--teal) 0%, var(--ocean) 45%, var(--deep-blue) 100%);
    font-family: "Fira Sans Extra Condensed", "Arial Narrow", sans-serif;
  }

  .flight-paths { position: absolute; inset: 0; }

  .brand-owner {
    position: absolute;
    left: 186px; top: 36px;
    font-family: "Open Sans", sans-serif;
    font-weight: 600;
    font-size: 24px;
    letter-spacing: -0.3px;
    color: var(--white);
  }
  .brand-name {
    position: absolute;
    left: 190px; top: 78px;
    font-family: "Fira Sans Extra Condensed", sans-serif;
    font-weight: 800;
    font-size: 92px;
    line-height: 1;
    color: var(--brown);
  }

  .target { position: absolute; left: 95px; top: 195px; width: 330px; height: 330px; }
  .target-art {
    position: absolute;
    left: 170px; top: 255px;
    width: 200px; height: 200px;
    border-radius: 45%;
    background: radial-gradient(ellipse at 50% 45%, #e6d3b5 0%, #f1e5d2 45%, rgba(255,255,255,0) 72%);
  }

  .headline-panel {
    position: absolute;
    left: 596px; top: -40px;
    width: 522px; height: 240px;
    background: var(--brown);
    border-radius: 0 0 44px 44px;
    text-align: center;
    padding-top: 62px;
  }
  .headline {
    font-weight: 800;
    line-height: 0.9;
    text-transform: uppercase;
    text-shadow: 4px 4px 0 var(--brown-shadow);
  }
  .headline-top { display: block; font-size: 80px; color: var(--teal-bright); }
  .headline-bottom { display: block; font-size: 80px; color: var(--white); }

  .product-type {
    position: absolute;
    left: 630px; top: 232px;
    width: 460px;
    text-align: center;
    font-family: "Dancing Script", cursive;
    font-weight: 700;
    line-height: 0.82;
    text-shadow: 3px 3px 0 var(--shade);
  }
  .product-type-main { display: block; font-size: 68px; color: var(--white); }
  .product-type-sub { display: block; font-size: 64px; color: var(--teal-bright); margin-left: -30px; }

  .info-panel {
    position: absolute;
    left: 524px; top: 398px;
    width: 700px; height: 180px;
    background: var(--brown);
    border-radius: 40px 0 0 0;
  }
  .ingredients {
    position: absolute;
    left: 80px; top: 24px;
    width: 550px;
    font-weight: 400;
    font-size: 22px;
    line-height: 1.22;
    color: var(--white);
    text-align: center;
  }
  .formulators {
    position: absolute;
    left: 80px; top: 90px;
    width: 520px;
    font-weight: 400;
    font-size: 18px;
    color: var(--teal-bright);
    text-align: center;
  }
  .net-weight,
  .origin-contact {
    position: absolute;
    top: 118px;
    font-weight: 400;
    font-size: 18px;
    color: var(--cream);
  }
  .net-weight { left: 68px; }
  .origin-contact { right: 56px; }
</style>
</head>
<body>
  <main class="label">
    <svg class="flight-paths" width="1200" height="558" viewBox="0 0 1200 558" aria-hidden="true">
      <g fill="none" stroke="var(--path)" stroke-width="1.6" stroke-dasharray="4 6">
        <path d="M80 245 C 30 330, 60 470, 140 558"/>
        <path d="M360 230 C 460 200, 540 260, 520 330 C 500 400, 430 440, 390 558"/>
        <path d="M470 150 C 420 180, 380 200, 360 230"/>
      </g>
    </svg>

    <p class="brand-owner">Rob and Jo’s</p>
    <p class="brand-name">G2M</p>

    <svg class="target" viewBox="0 0 330 330" aria-hidden="true">
      <circle cx="170" cy="170" r="154" fill="#1a5f95" opacity="0.45"/>
      <circle cx="165" cy="165" r="154" fill="var(--white)" stroke="var(--brown)" stroke-width="12"/>
      <g stroke="var(--brown)" stroke-width="11">
        <line x1="165" y1="8" x2="165" y2="36"/>
        <line x1="165" y1="294" x2="165" y2="322"/>
        <line x1="8" y1="165" x2="36" y2="165"/>
        <line x1="294" y1="165" x2="322" y2="165"/>
      </g>
    </svg>
    <div class="target-art" role="img" aria-label="Illustration of a sandfly in the target sight"></div>

    <header class="headline-panel">
      <h1 class="headline">
        <span class="headline-top">Goodbye to</span>
        <span class="headline-bottom">Midge bites!</span>
      </h1>
    </header>

    <h2 class="product-type">
      <span class="product-type-main">Natural Sandfly</span>
      <span class="product-type-sub">Repellent</span>
    </h2>

    <section class="info-panel">
      <p class="ingredients">Contains Essential Oils of cedar wood, rosemary, cinnamon, citronella, lavender, eucalyptus and clove in a moisturising base.</p>
      <p class="formulators">Formulated by Australian Pharmacists Carla Whitby and Rob Kettering</p>
      <span class="net-weight">50 grams</span>
      <span class="origin-contact">Made in Australia • 0413862207</span>
    </section>
  </main>
</body>
</html>
```